New Corporate Business Card - Velmorana

What we need:
We need a new corporate business card.
We want a new template that we can change by ourself.
We want business card modern and minimalist but that looks professional.
We will print it in 300 gr soft-touch.
Why not a white side with the logo and a red/grey side with the content?
Why not a grey side and a red side like our logo?
I am sure that you have better idea than ours that's the reason we come here.

Who we are:
We are a private label company in cosmetics based in Switzerland. We work in BtoB. We make skin care products for other brands.

Target Market(s)

B to B - Worldwide - any gender

Industry/Entity Type

Cosmetics

Contact Information for Business Card

Side 1:
Logo
Your Swiss Private Label Manufacturer or www.velmorana-example.ch

Side 2:
Name and surname (Example: Lucien Marchetaz)
Job Description (General Manager)
Telephone (+41 32 915 63 00)
Direct (+41 32 915 63 63)
Email (lucien.marchetaz@velmorana-example.ch)
Chemin des Pélerines 14, 2000 Neuchâtel, Switzerland
www.velmorana-example.ch

Font styles to use
Serif
Sans Serif

Requirements
Must have
• You can use 4 colors: white, red, grey and/or black .
Should not have
• Too much colors, too much things. We want it simple!

```html
<!DOCTYPE html>
<html lang="en">
<head>
<meta charset="utf-8">
<title>Velmorana – Business Card</title>
<link rel="stylesheet" href="https://fonts.googleapis.com/css2?family=Lato:wght@300;400;700&display=swap">
<style>
  :root {
    --red: #ee2b3b;
    --grey: #a8a9ac;
    --ink: #1c1c1c;
    --white: #ffffff;
    --backdrop: #5c5c5c;
  }
  * { box-sizing: border-box; margin: 0; padding: 0; }
  html, body { width: 1200px; height: 802px; overflow: hidden; }
  body {
    background: var(--backdrop);
    font-family: "Lato", sans-serif;
    position: relative;
  }
  .card {
    position: absolute;
    top: 274px;
    width: 442px;
    height: 265px;
    overflow: hidden;
    box-shadow: 2px 3px 6px rgba(0,0,0,0.35);
  }
  /* Contact side */
  .card--contact { left: 136px; background: var(--grey); }
  .contact__band {
    position: absolute; left: 0; top: 0;
    width: 100%; height: 81px;
    background: var(--red);
  }
  .contact__tab {
    position: absolute; left: 244px; top: 28px;
    width: 142px; height: 60px;
    background: var(--grey);
  }
  .brand {
    position: absolute;
    display: flex; align-items: center; gap: 8px;
    color: var(--white);
    font-weight: 300;
    letter-spacing: 0.12em;
  }
  .brand__square {
    border: 2px solid var(--white);
    flex: none;
  }
  .contact__brand { left: 255px; top: 44px; font-size: 17px; }
  .contact__brand .brand__square { width: 12px; height: 12px; }

  .contact__details {
    position: absolute; left: 24px; top: 113px;
    color: var(--ink);
  }
  .contact__name {
    font-size: 16.5px; font-weight: 700; line-height: 1.1;
    text-transform: uppercase; letter-spacing: -0.01em;
  }
  .contact__role { font-size: 12.5px; margin-bottom: 6px; }
  .contact__list { list-style: none; font-size: 12px; line-height: 15.6px; }
  .contact__list li { display: flex; align-items: center; gap: 4px; }
  .contact__list svg { width: 10px; height: 10px; flex: none; fill: var(--ink); }
  .contact__note { font-size: 10px; }
  .contact__address { font-size: 12.5px; line-height: 15.6px; margin-top: 5px; }

  /* Brand side */
  .card--brand { left: 624px; background: var(--red); }
  .brand-side__brand {
    left: 0; right: 0; top: 108px;
    justify-content: center;
    font-size: 38px;
  }
  .brand-side__brand .brand__square { width: 24px; height: 24px; border-width: 3px; }
  .brand-side__tagline {
    position: absolute; left: 0; right: 0; top: 222px;
    text-align: center;
    color: var(--white);
    font-size: 12px;
    text-transform: uppercase;
  }
</style>
</head>
<body>
  <section class="card card--contact">
    <div class="contact__band"></div>
    <div class="contact__tab"></div>
    <div class="brand contact__brand"><span class="brand__square"></span>Velmorana</div>

    <div class="contact__details">
      <h1 class="contact__name">Lucien Marchetaz</h1>
      <p class="contact__role">General Manager</p>
      <ul class="contact__list">
        <li><svg viewBox="0 0 10 10"><path d="M1 3.5C1 2 2.5 1.5 5 1.5S9 2 9 3.5V4.5H7V3.5H3V4.5H1Z M2.5 5L3.5 4H6.5L7.5 5V8.5H2.5Z"/></svg>+41 32 915 63 00</li>
        <li><svg viewBox="0 0 10 10"><path d="M1 3.5C1 2 2.5 1.5 5 1.5S9 2 9 3.5V4.5H7V3.5H3V4.5H1Z M2.5 5L3.5 4H6.5L7.5 5V8.5H2.5Z"/></svg>+41 32 915 63 63 <span class="contact__note">(DIRECT)</span></li>
        <li><svg viewBox="0 0 10 10"><path d="M1 2.5H9V7.5H1Z" /><path d="M1.3 2.8L5 5.5L8.7 2.8" fill="none" stroke="#a8a9ac" stroke-width="0.8"/></svg>lucien.marchetaz@velmorana-example.ch</li>
        <li><svg viewBox="0 0 10 10"><circle cx="5" cy="5" r="4.3"/><path d="M3 3.5L5 3L6 4.5L4.5 6L5 8" fill="none" stroke="#a8a9ac" stroke-width="0.9"/></svg>www.velmorana-example.ch</li>
      </ul>
      <p class="contact__address">Chemin des Pélerines 14<br>2000 Neuchâtel, Switzerland</p>
    </div>
  </section>

  <section class="card card--brand">
    <div class="brand brand-side__brand"><span class="brand__square"></span>Velmorana</div>
    <p class="brand-side__tagline">Your Swiss Private Label Manufacturer</p>
  </section>
</body>
</html>
```